MODELS AGENCY NEW YEAR 2026 CARD

A 10 cm x 21 cm horizontal New Year card for clients of our 2 models agencies, Brindel (kids) and Pavaduel (actors and adults) (logo in the jobs).

Side A of the card: creative mission:
-text: 2026
-text: Peace and Love
-Studio or movie set atmosphere
-tone of voice: optimistic, positive, colorful

Side B:
(name of 4 people of the agency:)
Solange, Anne-Sophie, Josiane & Paul-Henri,
(2 logos)
Brindel & PavaDuel
(Adres)
Rue des Tilleuls 74 b3 - 1060 Bruxelles - Belgique

Target Market(s)

Movie directors, photographers

Industry/Entity Type

Fashion, advertising & Movies

Requirements
Must have
• SEE TEXT IN BRIEFING

```html
<!DOCTYPE html>
<html lang="en">
<head>
<meta charset="utf-8">
<title>New Year 2026 Card</title>
<link rel="stylesheet" href="https://fonts.googleapis.com/css2?family=Montserrat:wght@300;400;600&display=swap">
<style>
  :root {
    --backdrop: #2e2e2e;
    --ink-black: #000000;
    --paper: #ffffff;
    --text-dark: #141414;
    --agency-orange: #e0531f;
    --agency-violet: #3b1f5c;
    --agency-blue: #1a9ad6;
    --screen-green: #7fa53a;
    --studio-dark: #1f1d16;
  }
  * { margin: 0; padding: 0; box-sizing: border-box; }
  html, body {
    width: 1200px; height: 1200px; overflow: hidden;
    background: var(--backdrop);
    font-family: "Montserrat", sans-serif;
  }
  .canvas { position: relative; width: 1200px; height: 1200px; }

  /* Side A */
  .card-front {
    position: absolute; left: 98px; top: 114px;
    width: 1004px; height: 478px;
    background: var(--ink-black); overflow: hidden;
  }
  .year {
    position: absolute; left: 160px; top: 108px;
    font-weight: 300; font-size: 198px; line-height: 0;
    color: var(--paper); letter-spacing: 2px;
  }
  .wish {
    position: absolute; left: 683px; top: 56px;
    font-weight: 300; font-size: 47px; line-height: 40px;
    color: var(--paper); letter-spacing: 1px;
  }
  .studio-scene {
    position: absolute; left: 0; top: 184px; width: 100%; height: 294px;
    background:
      radial-gradient(ellipse 130px 150px at 37% 62%, rgba(255,244,228,0.95), rgba(255,240,220,0.55) 55%, transparent 75%),
      radial-gradient(ellipse 70px 110px at 48% 65%, rgba(250,246,235,0.9), transparent 80%),
      radial-gradient(ellipse 170px 110px at 77% 70%, rgba(170,220,150,0.95), rgba(120,180,100,0.6) 60%, transparent 85%),
      var(--ink-black);
  }

  /* Side B */
  .card-back {
    position: absolute; left: 99px; top: 620px;
    width: 1001px; height: 476px;
    background: var(--paper); overflow: hidden;
  }
  .studio-detail {
    position: absolute; inset: 0;
    background:
      radial-gradient(ellipse 70px 90px at 80% 52%, rgba(255,230,190,0.9), transparent 80%),
      radial-gradient(ellipse 120px 140px at 50% 22%, rgba(255,240,225,0.85), transparent 80%),
      linear-gradient(90deg, var(--paper) 0%, var(--paper) 31%, #dfe2d2 43%, #a8b66f 55%, var(--screen-green) 68%, #556a22 86%, var(--studio-dark) 100%);
  }
  .team {
    position: absolute; left: 39px; top: 36px;
    font-weight: 600; font-size: 19px; line-height: 23px;
    color: var(--text-dark); list-style: none;
  }
  .address {
    position: absolute; left: 39px; top: 138px;
    font-weight: 400; font-size: 19px; line-height: 24px;
    color: var(--text-dark);
  }
  .agency {
    position: absolute; top: 350px;
    text-align: center; color: var(--agency-violet);
  }
  .agency-name {
    display: flex; align-items: center; justify-content: center; gap: 6px;
    font-weight: 600; font-size: 24px; line-height: 28px;
  }
  .agency-mark { width: 10px; height: 10px; border-radius: 50%; }
  .agency-tagline { font-size: 6px; letter-spacing: 0.6px; margin-top: 4px; font-weight: 400; }
  .agency-since { font-size: 4.5px; margin-top: 18px; font-weight: 400; }
  .agency-adults { left: 47px; width: 118px; }
  .agency-adults .agency-mark { background: var(--agency-orange); }
  .agency-kids { left: 188px; width: 120px; }
  .agency-kids .agency-mark { background: var(--agency-blue); }
</style>
</head>
<body>
<div class="canvas">
  <section class="card-front">
    <div class="studio-scene" role="img" aria-label="Photograph of a film studio set at night: a crew in silhouette before a lit white screen, curtains, light stands, a ladder and a green screen"></div>
    <div class="year" style="top:108px;line-height:1;">2026</div>
    <div class="wish">PEACE<br>AND<br>LOVE</div>
  </section>

  <section class="card-back">
    <div class="studio-detail" role="img" aria-label="Photograph of studio lighting gear: a reflector panel, light stands and a spotlight on a green screen, fading into white"></div>
    <ul class="team">
      <li>Solange</li>
      <li>Anne-Sophie</li>
      <li>Josiane</li>
      <li>Paul-Henri</li>
    </ul>
    <p class="address">Rue des Tilleuls 74 b3<br>- 1060 Bruxelles - Belgique</p>

    <div class="agency agency-adults">
      <div class="agency-name"><span class="agency-mark"></span>Pavaduel</div>
      <div class="agency-tagline">PEOPLE, ACTORS &amp; MODELS AGENCY</div>
      <div class="agency-since">– SINCE 2000 –</div>
    </div>
    <div class="agency agency-kids">
      <div class="agency-name"><span class="agency-mark"></span>Brindel</div>
      <div class="agency-tagline">CHILDREN MODELS AGENCY</div>
      <div class="agency-since">– SINCE 1982 –</div>
    </div>
  </section>
</div>
</body>
</html>
```